High end business card design for custom homebuilding company

Looking for a high end business card design that is unique and elegant. Can use embossing, foil printing, laser die cutting, or any high end printing technique or high end paper. Will upload current design so you can see the logo and what we are using currently, but we want something more unique and elegant. I included our logo to help with design.

Target Market(s)

High end custom home buyers of $1.5 million plus homes. Also real estate developers of high end communities.

Industry/Entity Type

Business

Contact Information for Business Card

Double sided. We want something very elegant and expensive looking. We are looking to incorporate a combination of perhaps linen paper or a high end paper, with foil stamping or embossing/debossing to make the card look unique, but still elegant. We tend to use blacks and golds, but are open to any ideas. Looking for creative and unique design.

Colors

Designer to choose colors to be used in the design.

Requirements
Must have
• High end, elegant look. Can use foil, embossing, or high end papers like linen. We want to make the card unique and interesting, but elegant and expensive looking.
Nice to have
• I am including just some cards I saw that looked interesting for one reason or another. I like a clean elegant design and like both the clean white style, and the blacks. So not sure if we want a black design or white. Would like to see both.

```html
<!DOCTYPE html>
<html lang="en">
<head>
<meta charset="utf-8">
<title>Halden Ridge Custom Homes – Business Card</title>
<link rel="stylesheet" href="https://fonts.googleapis.com/css2?family=Cinzel:wght@400&family=Open+Sans:wght@400;600&display=swap">
<style>
  :root {
    --backdrop: #5a3d29;
    --card: #262626;
    --silver: #c9c9c9;
    --white: #f4f4f4;
    --gold: #cfc03a;
    --gold-deep: #b9a92a;
    --text: #ececec;
  }
  * { margin: 0; padding: 0; box-sizing: border-box; }
  html, body { width: 1200px; height: 1000px; overflow: hidden; }
  body {
    position: relative;
    background: var(--backdrop);
    font-family: "Open Sans", Arial, sans-serif;
  }
  .card {
    position: absolute;
    left: 267px;
    width: 665px;
    height: 397px;
    background: var(--card);
    overflow: hidden;
  }
  .card--front { top: 75px; }
  .card--back { top: 533px; }

  .wordmark {
    font-family: "Cinzel", Georgia, serif;
    font-weight: 400;
    text-transform: uppercase;
    line-height: 1;
  }
  .card--front .wordmark {
    position: absolute;
    left: 0; right: 0; top: 180px;
    text-align: center;
    color: var(--silver);
  }
  .wordmark__name { display: block; font-size: 46px; letter-spacing: 1px; }
  .wordmark__tag { display: block; font-size: 17px; letter-spacing: 9px; margin-top: 4px; }

  .card--back .wordmark {
    position: absolute;
    left: 33px; top: 50px;
    color: var(--white);
  }
  .card--back .wordmark__name { font-size: 40px; }
  .card--back .wordmark__tag { font-size: 15px; letter-spacing: 8px; margin-top: 2px; }

  .contact {
    position: absolute;
    left: 32px; top: 148px;
    color: var(--text);
  }
  .contact__name {
    font-size: 19px;
    font-weight: 600;
    color: var(--gold);
    letter-spacing: 0.5px;
  }
  .contact__role { font-size: 15px; margin-top: 1px; }
  .contact__address { font-size: 15px; line-height: 20px; margin-top: 18px; }
  .contact__list { list-style: none; margin-top: 16px; }
  .contact__list li {
    display: flex; align-items: center;
    font-size: 15px; height: 24px;
  }
  .contact__list svg { width: 14px; height: 14px; margin-right: 8px; flex: none; }

  .foil-band {
    position: absolute;
    left: 0; right: 0; bottom: 0;
    height: 13px;
    background: linear-gradient(90deg, var(--gold-deep), var(--gold) 50%, var(--gold-deep));
  }
</style>
</head>
<body>
  <section class="card card--front" aria-label="Card front">
    <div class="wordmark">
      <span class="wordmark__name">Halden Ridge</span>
      <span class="wordmark__tag">Custom Homes</span>
    </div>
  </section>

  <section class="card card--back" aria-label="Card back">
    <div class="wordmark">
      <span class="wordmark__name">Halden Ridge</span>
      <span class="wordmark__tag">Custom Homes</span>
    </div>

    <div class="contact">
      <p class="contact__name">DANIEL ARCHER</p>
      <p class="contact__role">Managing Director</p>
      <p class="contact__address">2471 Marrow Creek Lane,<br>Seabrook Harbor FL 32190</p>
      <ul class="contact__list">
        <li>
          <svg viewBox="0 0 14 14" aria-hidden="true"><circle cx="7" cy="7" r="6.5" fill="var(--gold)"/></svg>
          @HaldenRidgeHomes
        </li>
        <li>
          <svg viewBox="0 0 14 14" aria-hidden="true"><path d="M3 1.5l2.2 0.3 0.9 2.8-1.4 1.1c0.8 1.6 2 2.8 3.6 3.6l1.1-1.4 2.8 0.9 0.3 2.2c-0.3 0.8-1 1.2-1.8 1.2C5.4 12.2 1.8 8.6 1.8 3.3c0-0.8 0.4-1.5 1.2-1.8z" fill="var(--gold)"/></svg>
          + 555 010 0199
        </li>
        <li>
          <svg viewBox="0 0 14 14" aria-hidden="true"><rect x="1" y="3" width="12" height="8.5" fill="var(--gold)"/><path d="M1 3.3l6 4.4 6-4.4" stroke="var(--card)" stroke-width="1.1" fill="none"/></svg>
          info@haldenridgehomes.com
        </li>
        <li>
          <svg viewBox="0 0 14 14" aria-hidden="true"><g fill="none" stroke="var(--gold)" stroke-width="1.2"><circle cx="7" cy="7" r="5.8"/><ellipse cx="7" cy="7" rx="2.5" ry="5.8"/><path d="M1.2 7h11.6M2.2 4h9.6M2.2 10h9.6"/></g></svg>
          info@haldenridgehomes.com
        </li>
      </ul>
    </div>

    <div class="foil-band"></div>
  </section>
</body>
</html>
```